Harbor Decals
Vending Solutions for your Business
Harbor Decals -
Creative Brief
Bright & Fun-filled
Dale Whitcombe
Owner
24870 Pellwood Lane San Jose, CA 95031
harbor.decals@pellmail.net
Use logo on card and stationary

```html
<!DOCTYPE html>
<html lang="en">
<head>
<meta charset="utf-8">
<title>Harbor Decals Stationery</title>
<link href="https://fonts.googleapis.com/css2?family=Open+Sans:wght@400;700&display=swap" rel="stylesheet">
<style>
:root{
  --bg:#e9e6e2;
  --paper:#ffffff;
  --orange:#f39200;
  --purple:#3b2a8c;
  --red:#c8102e;
  --ink:#333333;
  --muted:#8a8a8a;
  --faint:#f6efe4;
}
*{margin:0;padding:0;box-sizing:border-box}
html,body{width:1200px;height:341px;overflow:hidden;background:var(--bg);font-family:"Open Sans",Arial,sans-serif;color:var(--ink)}
.canvas{position:relative;width:1200px;height:341px}
.sheet{position:absolute;background:var(--paper);box-shadow:0 2px 5px rgba(0,0,0,.18);overflow:hidden}
.brand{display:flex;align-items:center;gap:4px;font-weight:700;color:var(--purple);white-space:nowrap}
.brand-dot{border-radius:50%;background:var(--orange);flex:none}
.tagline{font-size:5px;color:var(--muted)}
.swoosh{position:absolute;left:0;bottom:0;width:100%}
.watermark{position:absolute;border-radius:50%;background:var(--faint)}
.tiny{position:absolute;font-size:3.5px;color:var(--muted);line-height:1.3}

.main-brand{position:absolute;left:22px;top:62px}
.main-brand .brand{font-size:15px}
.main-brand .brand-dot{width:16px;height:16px}
.main-brand .tagline{font-size:6px;margin-top:2px;margin-left:20px}

.biz-card{left:19px;width:132px;height:84px}
.biz-card .brand{position:absolute;left:8px;top:10px;font-size:10px}
.biz-card .brand-dot{width:11px;height:11px}
.card-contact{position:absolute;left:8px;top:32px;font-size:4.5px;line-height:1.45;color:var(--ink)}
.card-contact b{font-size:5.5px;color:var(--purple)}

.letterhead{top:24px;width:196px;height:288px}
.letterhead .brand{position:absolute;left:14px;top:14px;font-size:11px}
.letterhead .brand-dot{width:12px;height:12px}
.letterhead .watermark{left:48px;top:94px;width:100px;height:100px}
.letterhead .tiny.head{right:14px;top:14px;text-align:right}
.letterhead .tiny.foot{left:0;right:0;bottom:18px;text-align:center}

.slip{left:643px;width:186px;height:112px}
.slip .brand{position:absolute;left:12px;top:12px;font-size:9px}
.slip .brand-dot{width:10px;height:10px}
.slip .watermark{left:68px;top:26px;width:50px;height:50px}
.slip .tiny{left:0;right:0;bottom:14px;text-align:center}

.envelope{left:840px;width:312px;height:106px}
.envelope svg.flap{position:absolute;left:0;top:0;width:100%;height:60px}
.envelope .seal{position:absolute;left:50%;top:38px;width:22px;height:22px;margin-left:-11px;border-radius:50%;background:var(--orange);border:2px solid var(--paper)}
</style>
</head>
<body>
<div class="canvas">

  <div class="main-brand">
    <div class="brand"><span class="brand-dot"></span>Harbor Decals</div>
    <div class="tagline">Vending Solutions for your Business</div>
  </div>

  <div class="sheet biz-card" style="top:104px">
    <div class="brand"><span class="brand-dot"></span>Harbor Decals</div>
    <div class="card-contact"><b>Dale Whitcombe</b><br>Owner<br>24870 Pellwood Lane<br>San Jose, CA 95031<br>harbor.decals@pellmail.net</div>
    <svg class="swoosh" viewBox="0 0 132 20" height="20" preserveAspectRatio="none"><path d="M0 20 L132 20 L132 4 Q70 22 0 8Z" fill="var(--purple)"/><path d="M0 8 Q70 22 132 4 L132 7 Q70 25 0 11Z" fill="var(--orange)"/></svg>
  </div>
  <div class="sheet biz-card" style="top:210px">
    <div class="brand"><span class="brand-dot"></span>Harbor Decals</div>
    <div class="card-contact"><b>Dale Whitcombe</b><br>Owner<br>24870 Pellwood Lane<br>San Jose, CA 95031<br>harbor.decals@pellmail.net</div>
    <svg class="swoosh" viewBox="0 0 132 20" height="20" preserveAspectRatio="none"><path d="M0 20 L132 20 L132 4 Q70 22 0 8Z" fill="var(--purple)"/><path d="M0 8 Q70 22 132 4 L132 7 Q70 25 0 11Z" fill="var(--orange)"/></svg>
  </div>

  <div class="sheet letterhead" style="left:232px">
    <div class="brand"><span class="brand-dot"></span>Harbor Decals</div>
    <div class="tiny head">24870 Pellwood Lane<br>San Jose, CA 95031<br>harbor.decals@pellmail.net</div>
    <div class="watermark"></div>
    <div class="tiny foot">Vending Solutions for your Business</div>
    <svg class="swoosh" viewBox="0 0 196 16" height="16" preserveAspectRatio="none"><path d="M0 16 L196 16 L196 6 Q100 18 0 4Z" fill="var(--purple)"/><path d="M0 4 Q100 18 196 6 L196 9 Q100 21 0 7Z" fill="var(--orange)"/></svg>
  </div>
  <div class="sheet letterhead" style="left:436px">
    <div class="brand"><span class="brand-dot"></span>Harbor Decals</div>
    <div class="tiny head">24870 Pellwood Lane<br>San Jose, CA 95031<br>harbor.decals@pellmail.net</div>
    <div class="watermark"></div>
    <div class="tiny foot">Vending Solutions for your Business</div>
    <svg class="swoosh" viewBox="0 0 196 16" height="16" preserveAspectRatio="none"><path d="M0 16 L196 16 L196 6 Q100 18 0 4Z" fill="var(--purple)"/><path d="M0 4 Q100 18 196 6 L196 9 Q100 21 0 7Z" fill="var(--orange)"/></svg>
  </div>

  <div class="sheet slip" style="top:72px">
    <div class="brand"><span class="brand-dot"></span>Harbor Decals</div>
    <div class="watermark"></div>
    <div class="tiny">harbor.decals@pellmail.net</div>
    <svg class="swoosh" viewBox="0 0 186 12" height="12" preserveAspectRatio="none"><path d="M0 12 L186 12 L186 4 Q90 14 0 3Z" fill="var(--purple)"/><path d="M0 3 Q90 14 186 4 L186 6 Q90 16 0 5Z" fill="var(--orange)"/></svg>
  </div>
  <div class="sheet slip" style="top:206px">
    <div class="brand"><span class="brand-dot"></span>Harbor Decals</div>
    <div class="watermark"></div>
    <div class="tiny">harbor.decals@pellmail.net</div>
    <svg class="swoosh" viewBox="0 0 186 12" height="12" preserveAspectRatio="none"><path d="M0 12 L186 12 L186 4 Q90 14 0 3Z" fill="var(--purple)"/><path d="M0 3 Q90 14 186 4 L186 6 Q90 16 0 5Z" fill="var(--orange)"/></svg>
  </div>

  <div class="sheet envelope" style="top:60px">
    <svg class="flap" viewBox="0 0 312 60" preserveAspectRatio="none"><path d="M0 0 L312 0 L312 8 L156 52 L0 8Z" fill="var(--red)"/></svg>
    <div class="seal"></div>
  </div>
  <div class="sheet envelope" style="top:134px">
    <svg class="flap" viewBox="0 0 312 60" preserveAspectRatio="none"><path d="M0 0 L312 0 L312 8 L156 52 L0 8Z" fill="var(--purple)"/></svg>
    <div class="seal"></div>
  </div>
  <div class="sheet envelope" style="top:208px">
    <svg class="flap" viewBox="0 0 312 60" preserveAspectRatio="none"><path d="M0 0 L312 0 L312 8 L156 52 L0 8Z" fill="#f4f4f4" stroke="#dddddd" stroke-width="1"/></svg>
  </div>

</div>
</body>
</html>
```